Front and content page design for Fitness Cookbook

I am looking for someone to Design a front cover for a Recipe book and also create an amazing layout for the book.

Its for a corporate seminar so has to be eye catching, professional and bold.

Content is complete

Target Market(s)

Industry/Entity Type

Health And Wellness

Font styles to use
Sans Serif

Requirements
Must have
• Eye catching, professional and bold.
• By Dorian as stated on the document
• Must have Velmora Athletics Logo on it.

```html
<!DOCTYPE html>
<html lang="en">
<head>
<meta charset="utf-8">
<title>Pan Fried Asparagus – Recipe Page</title>
<link rel="stylesheet" href="https://fonts.googleapis.com/css2?family=Cabin:wght@400;500;600&display=swap">
<style>
  :root {
    --page-bg: #ffffff;
    --band-orange: #f7941d;
    --label-blue: #2b9fd8;
    --body-ink: #2b2b2b;
    --title-ink: #ffffff;
    --footer-ink: #5a6b7a;
    --photo-light: #f4f5f1;
    --photo-green: #b9c79a;
  }
  * { margin: 0; padding: 0; box-sizing: border-box; }
  html, body {
    width: 849px;
    height: 1200px;
    overflow: hidden;
    background: var(--page-bg);
  }
  .recipe-page {
    position: relative;
    width: 849px;
    height: 1200px;
    background: var(--page-bg);
    font-family: "Cabin", sans-serif;
    color: var(--body-ink);
  }
  .dish-photo {
    position: absolute;
    left: 0;
    top: 0;
    width: 849px;
    height: 495px;
    background:
      radial-gradient(ellipse 62% 22% at 52% 42%, var(--photo-green) 0%, rgba(185,199,154,0.55) 55%, rgba(244,245,241,0) 100%),
      linear-gradient(180deg, #fbfbfa 0%, var(--photo-light) 100%);
  }
  .title-band {
    position: absolute;
    left: 0;
    top: 495px;
    width: 849px;
    height: 170px;
    background: var(--band-orange);
    display: flex;
    align-items: center;
    justify-content: center;
  }
  .recipe-title {
    color: var(--title-ink);
    font-weight: 400;
    font-size: 52px;
    letter-spacing: 0.5px;
  }
  .recipe-body {
    position: absolute;
    left: 51px;
    top: 676px;
    width: 750px;
  }
  .timing {
    font-size: 15px;
    line-height: 22px;
  }
  .label {
    color: var(--label-blue);
    font-weight: 500;
    font-size: 17px;
    text-transform: uppercase;
    letter-spacing: 0.3px;
  }
  .section { margin-top: 26px; }
  .section-heading {
    color: var(--label-blue);
    font-weight: 500;
    font-size: 17px;
    text-transform: uppercase;
    letter-spacing: 0.3px;
    line-height: 22px;
  }
  .ingredient-list { list-style: none; }
  .ingredient-list li,
  .instructions {
    font-size: 14.5px;
    line-height: 20px;
  }
  .page-footer {
    position: absolute;
    left: 51px;
    top: 1148px;
    display: flex;
    align-items: center;
    gap: 10px;
    color: var(--footer-ink);
    font-size: 13px;
  }
  .brand {
    display: flex;
    align-items: center;
    gap: 5px;
    font-weight: 500;
    font-size: 12px;
  }
  .brand-dot {
    width: 12px;
    height: 12px;
    border-radius: 50%;
    background: var(--footer-ink);
  }
</style>
</head>
<body>
<main class="recipe-page">
  <div class="dish-photo" role="img" aria-label="Photograph of pan fried asparagus spears seasoned with paprika on a white plate"></div>

  <header class="title-band">
    <h1 class="recipe-title">Pan Fried Asparagus</h1>
  </header>

  <section class="recipe-body">
    <p class="timing"><span class="label">Prep time</span> 5 mins</p>
    <p class="timing"><span class="label">Cooking time</span> 10 mins</p>

    <div class="section">
      <h2 class="section-heading">Ingredients</h2>
      <ul class="ingredient-list">
        <li>1 pack asparagus</li>
        <li>1 tbsp natural butter</li>
        <li>salt, pepper, paprika</li>
      </ul>
    </div>

    <div class="section">
      <h2 class="section-heading">Cooking instructions</h2>
      <p class="instructions">Season the spears and melt the butter in a pan on a medium heat. Fry for 8-10 minutes until<br>slightly brown both sides.</p>
    </div>
  </section>

  <footer class="page-footer">
    <span class="page-number">28</span>
    <span class="brand"><span class="brand-dot"></span>Velmora Athletics</span>
  </footer>
</main>
</body>
</html>
```